Brand refresh of quote, work docket and Fire certificate documents

I would like a refresh of our document suit including

1. Front page called VOLT3 Proposal
2. Quote document template
3. Work docket template
4. Fire certificate template - to look like a professional complaint certificate

Examples of documents are attached.

```html
<!DOCTYPE html>
<html lang="en">
<head>
<meta charset="utf-8">
<title>VOLT3 Document Suite</title>
<link href="https://fonts.googleapis.com/css2?family=Roboto:wght@400;500;700;900&display=swap" rel="stylesheet">
<style>
:root{
  --bg:#adaaab;
  --paper:#ffffff;
  --dark:#2b2b2c;
  --ink:#222222;
  --muted:#555555;
  --rule:#c9c9c9;
  --orange:#f05a28;
  --red:#e63a2a;
  --faint:#f1f1f1;
}
*{margin:0;padding:0;box-sizing:border-box}
html,body{width:1200px;height:446px;overflow:hidden;background:var(--bg);font-family:"Roboto",Arial,sans-serif;color:var(--ink)}
.page{position:absolute;top:40px;width:262px;height:370px;background:var(--paper);overflow:hidden}
.p1{left:36px;background:var(--dark)}
.p2{left:322px}.p3{left:609px}.p4{left:897px}

/* cover */
.cover-photo{position:absolute;left:0;top:0;width:87px;height:370px;border-radius:0 18px 18px 0;background:linear-gradient(180deg,#e23a2c 0%,#ec5a2c 55%,#f48a3a 100%)}
.cover-logo{position:absolute;left:103px;top:130px;font-weight:900;font-size:44px;color:#fff;letter-spacing:1px;line-height:1}
.cover-tag{position:absolute;left:104px;top:177px;font-size:6.6px;color:#fff;letter-spacing:3.1px;white-space:nowrap}
.cover-foot{position:absolute;left:99px;top:336px;width:145px;height:14px;border-top:.6px solid #888;border-bottom:.6px solid #888;color:#fff;font-size:6px;letter-spacing:.4px;display:flex;align-items:center;justify-content:center;white-space:nowrap}

/* watermark */
.watermark{position:absolute;right:-70px;top:200px;transform:rotate(-90deg);font-weight:900;font-size:62px;color:var(--faint);letter-spacing:2px;white-space:nowrap}
.p2 .watermark{top:215px}

/* header */
.brand{position:absolute;left:30px;top:26px;font-weight:900;font-size:21px;color:var(--ink);line-height:1}
.brand-sub{position:absolute;left:30px;top:49px;font-size:2.8px;letter-spacing:1.2px;color:var(--muted);white-space:nowrap}
.doc-title{position:absolute;right:30px;top:35px;font-size:7px;font-weight:500;letter-spacing:2.2px}
.head-rule{position:absolute;left:30px;right:30px;top:45px;border-top:.6px solid var(--rule)}
.company{position:absolute;right:30px;top:25px;text-align:right;font-size:4.6px;line-height:7px;white-space:nowrap}
.company strong{font-size:7.5px;display:block;line-height:10px}
.rule-main{position:absolute;left:30px;right:30px;top:60px;border-top:.8px solid var(--rule)}
.rule-accent{position:absolute;left:167px;right:30px;top:59.5px;border-top:1.6px solid var(--orange)}
.docket-row{position:absolute;left:30px;right:30px;top:64px;height:12px;display:flex;justify-content:space-between;align-items:center;font-size:6.6px;font-weight:500;letter-spacing:2px;border-bottom:.6px solid var(--rule)}
.docket-row .date{font-size:5.2px;letter-spacing:1.5px}
.to{position:absolute;left:30px;top:85px;font-size:4.8px;line-height:7px}
.to b{font-size:5.4px}
.docket-no{position:absolute;right:30px;top:117px;font-size:4.8px;font-weight:500}
.intro{position:absolute;left:30px;right:30px;top:131px;font-size:4.8px;line-height:7px}

/* section badges and tables */
.badge{position:absolute;left:30px;right:30px;height:8px;display:flex;align-items:center}
.badge span{background:var(--dark);color:#fff;font-size:5px;font-weight:700;padding:0 3px;height:8px;line-height:8px;white-space:nowrap}
.badge::after{content:"";flex:1;border-top:.5px solid var(--rule);margin-left:2px}
table{position:absolute;left:30px;width:202px;border-collapse:collapse;table-layout:fixed;font-size:4.5px;line-height:6.8px;background:#fff;color:var(--ink)}
td{border:.5px solid var(--rule);vertical-align:top;padding:3px 4px 2px 7px}
td.loc{font-size:5px;padding-left:8px}
.tag{color:var(--red)}
.small{font-size:2.8px;display:block;line-height:4px}
.note{position:absolute;left:30px;top:114px;font-size:4.6px;font-weight:700;color:var(--red)}

/* footer */
.footer{position:absolute;left:30px;right:30px;top:332px;border-top:.6px solid #f3b3a0}
.footer .site{position:absolute;left:0;top:2px;font-size:3.8px;letter-spacing:1.2px}
.footer .num{position:absolute;right:0;top:0;width:12px;height:8px;background:var(--orange);color:#fff;font-size:4px;text-align:center;line-height:8px}
</style>
</head>
<body>

<section class="page p1">
  <div class="cover-photo" role="img" aria-label="Photo of installer working on a scissor lift in a fire-protected ceiling space, tinted red to orange"></div>
  <div class="cover-logo">VOLT3</div>
  <div class="cover-tag">PASSIVE FIRE PROTECTION</div>
  <div class="cover-foot">COMPANY PROPOSAL &nbsp;|&nbsp; www.volt3.com.au</div>
</section>

<section class="page p2">
  <div class="watermark">VOLT3</div>
  <div class="brand">VOLT3</div>
  <div class="brand-sub">PASSIVE FIRE PROTECTION</div>
  <div class="company"><strong>VOLT3 PTY LTD</strong>4/22 Banksia Street Ringwood VIC 3134<br>ABN: 48 602 115 904<br>admin@volt3.com.au</div>
  <div class="rule-main"></div><div class="rule-accent"></div>
  <div class="docket-row"><span>WORK DOCKET</span><span class="date">20TH JULY, 2026</span></div>
  <div class="to"><b>TO</b><br><b>MARCHETTI BUILDERS</b><br>118 Wharf St Docklands<br>Melbourne VIC 3008<br><b>Lorenzo</b></div>
  <div class="docket-no">Work Docket: 1188</div>
  <div class="intro">Works completed at 14 Ashby Street, Essendon as directed by Lorenzo of Marchetti Builders as listed below.</div>
  <div class="badge" style="top:151px"><span>WORKS COMPLETED</span></div>
  <table style="top:162px">
    <colgroup><col style="width:48px"><col style="width:39px"><col style="width:38px"><col></colgroup>
    <tr style="height:20px"><td class="loc">Basement 1</td><td>Fan<br>Room</td><td>1 x 20mm<br>x 20mm</td><td>Penetration with Conduit Through Blockwork Wall <span class="tag">(?)</span></td></tr>
    <tr style="height:26px"><td class="loc">Basement 1</td><td>Apartment<br>38 Garage</td><td>2 x 100mm<br>x 100mm</td><td>Penetration with Sprinkler Pipe &amp; Wrap through Slab Wall <span class="tag">(Wet Fire)</span></td></tr>
    <tr style="height:26px"><td class="loc">Basement 1</td><td>Apartment<br>34 Garage</td><td>2 x 100mm<br>x 100mm</td><td>Penetration with Sprinkler Pipe &amp; Wrap through Slab Wall <span class="tag">(Wet Fire)</span></td></tr>
    <tr style="height:27px"><td class="loc">Basement 1</td><td>Apartment<br>30 Garage</td><td>2 x 100mm<br>x 100mm</td><td>Penetration with Sprinkler Pipe &amp; Wrap through Slab Wall <span class="tag">(Wet Fire)</span></td></tr>
    <tr style="height:26px"><td class="loc">Basement 1</td><td>Apartment<br>34 Garage</td><td>2 x 100mm<br>x 100mm</td><td>Penetration with Sprinkler Pipe &amp; Wrap through Slab Wall <span class="tag">(Wet Fire)</span></td></tr>
    <tr style="height:26px"><td class="loc">Basement 1</td><td>Apartment<br>28</td><td>5mtrs</td><td>of caulking through slab wall (one side only)<br><span class="tag">(Brickies)</span></td></tr>
  </table>
  <div class="footer"><span class="site">www.volt3.com.au</span><span class="num">02</span></div>
</section>

<section class="page p3">
  <div class="watermark">VOLT3</div>
  <div class="brand">VOLT3</div>
  <div class="brand-sub">PASSIVE FIRE PROTECTION</div>
  <div class="doc-title">WORK DOCKET</div>
  <div class="head-rule"></div>
  <div class="badge" style="top:62px"><span>WORKS COMPLETED</span></div>
  <table style="top:72px">
    <colgroup><col style="width:48px"><col style="width:39px"><col style="width:38px"><col></colgroup>
    <tr style="height:19px"><td class="loc">Basement 1</td><td>Back<br>Stairwell</td><td>1 x 400mm<br>x 400mm</td><td>Penetration Empty through Blockwork Wall <span class="tag">(Builder)</span></td></tr>
    <tr style="height:23px"><td class="loc" rowspan="3">Basement 1</td><td rowspan="3">Apartment<br>Bin Room</td><td>1 x 80mm x<br>80mm</td><td>Penetration with Sprinkler Pipe &amp; Wrap Through Blockwork Wall <span class="tag">(Wet Fire)</span></td></tr>
    <tr style="height:18px"><td>2 x 20mm x<br>20mm</td><td>Penetration with Conduit through Blockwork Wall <span class="tag">(?)</span></td></tr>
    <tr style="height:19px"><td>2 x 20mm x<br>20mm</td><td>Penetration with Conduit through Blockwork Wall <span class="tag">(?)</span></td></tr>
    <tr style="height:19px"><td class="loc">Basement 1</td><td>Comms<br>Room</td><td>2 x 300mm<br>x 300mm</td><td>Penetration Empty Through Slab Wall <span class="tag">(Builder)</span></td></tr>
    <tr style="height:19px"><td class="loc" rowspan="2">Basement 1</td><td rowspan="2">Switchboard<br>Room</td><td>1 x 400mm<br>x 100mm</td><td>Penetration Empty through Blockwork Wall <span class="tag">(Builder)</span></td></tr>
    <tr style="height:17px"><td>12mtrs</td><td>of caulking through blockwork wall (one side only) <span class="tag">(Brickies)</span></td></tr>
  </table>
  <div class="badge" style="top:214px"><span>LABOUR</span></div>
  <table style="top:224px">
    <colgroup><col style="width:48px"><col style="width:77px"><col></colgroup>
    <tr style="height:15px"><td>21/10/23</td><td>2 Men x 5hrs = 10hrs<span class="small">(time &amp; a half rate)</span></td><td>$1500.00</td></tr>
  </table>
  <div class="badge" style="top:247px"><span>MATERIALS</span></div>
  <table style="top:257px">
    <colgroup><col style="width:125px"><col></colgroup>
    <tr style="height:9.3px"><td style="padding:1px 4px 1px 8px">1 x Fire Mortar (20kg bag)</td><td style="padding:1px 4px 1px 9px">$150.00</td></tr>
    <tr style="height:9.3px"><td style="padding:1px 4px 1px 8px">2 x Rod (Bundle)</td><td style="padding:1px 4px 1px 9px">$100.00</td></tr>
    <tr style="height:9.3px"><td style="padding:1px 4px 1px 8px">$100.00 15 x Caulk (Ltr)</td><td style="padding:1px 4px 1px 9px">$375.00</td></tr>
    <tr style="height:9.3px"><td style="padding:1px 4px 1px 8px">$375.00 4 x KTX 300ml</td><td style="padding:1px 4px 1px 9px">$120.00</td></tr>
    <tr style="height:9.3px"><td style="padding:1px 4px 1px 8px">$120.00 1 x Ardentwrap 40 (Roll)</td><td style="padding:1px 4px 1px 9px">$220.00</td></tr>
    <tr style="height:9.3px"><td style="padding:1px 4px 1px 8px">$220.00 ¾ x Corvel Wrap (Roll)</td><td style="padding:1px 4px 1px 9px">$450.00</td></tr>
  </table>
  <div class="footer"><span class="site">www.volt3.com.au</span><span class="num">03</span></div>
</section>

<section class="page p4">
  <div class="watermark">VOLT3</div>
  <div class="brand">VOLT3</div>
  <div class="brand-sub">PASSIVE FIRE PROTECTION</div>
  <div class="doc-title">WORK DOCKET</div>
  <div class="head-rule"></div>
  <div class="badge" style="top:62px"><span>BREAKDOWN</span></div>
  <table style="top:71px">
    <colgroup><col style="width:124px"><col></colgroup>
    <tr style="height:9.8px"><td style="padding:1px 4px 1px 9px">Conduits (unknown)</td><td style="padding:1px 4px 1px 10px">10% - 291.50 + GST</td></tr>
    <tr style="height:9.8px"><td style="padding:1px 4px 1px 9px">Wet Fire</td><td style="padding:1px 4px 1px 10px">45% - $1,311 + GST</td></tr>
    <tr style="height:9.8px"><td style="padding:1px 4px 1px 9px">Brickies</td><td style="padding:1px 4px 1px 10px">20% - $583 + GST</td></tr>
    <tr style="height:9.8px"><td style="padding:1px 4px 1px 9px">Builder</td><td style="padding:1px 4px 1px 10px">20% - $583 + GST</td></tr>
  </table>
  <div class="note">**Price for Labour &amp; Materials - TOTAL: $2,915 + GST</div>
  <div class="footer"><span class="site">www.volt3.com.au</span><span class="num">04</span></div>
</section>

</body>
</html>
```